Visitenkarten-Design für Yogakurse
Zielgruppe
Ich biete Yogakurse für alle an sowieso speziell Yogakurse für Schwangere, frischgebackene Mamas und Rückbildungskurse.
Meine Zielgruppe sind hauptsächlich schwangere Frauen sowieso Frauen mit Babys.
Aufgabenstellung
Folgende Informationen sollten enthalten sein:
Ruhe im Kreis
Yoga & Beckenbodentraining
Mareike Holsten
info@ruhe-im-kreis-beispiel.de
www.ruhe-im-kreis-beispiel.de

```html
<!DOCTYPE html>
<html lang="de">
<head>
<meta charset="utf-8">
<title>Ruhe im Kreis – Visitenkarte</title>
<link rel="stylesheet" href="https://fonts.googleapis.com/css2?family=Open+Sans:wght@400;600&family=Allura&display=swap">
<style>
  :root {
    --sage: #dce5c6;
    --paper: #ffffff;
    --ink: #5b6450;
    --gold: #c29d58;
    --sand: #d8c3a2;
    --page: #ffffff;
  }
  * { margin: 0; padding: 0; box-sizing: border-box; }
  html, body { width: 1200px; height: 435px; overflow: hidden; background: var(--page); }
  .canvas { position: relative; width: 1200px; height: 435px; font-family: "Open Sans", Arial, sans-serif; color: var(--ink); }

  .card { position: absolute; top: 45px; width: 511px; height: 331px; background: var(--sage);
          box-shadow: 0 10px 24px rgba(0,0,0,0.12); overflow: hidden; }
  .card--front { left: 40px; }
  .card--back  { left: 612px; }

  .panel { position: absolute; top: 39px; height: 253px; background: var(--paper); }
  .card--front .panel { left: 0; width: 240px; border-radius: 0 28px 28px 0; }
  .card--back .panel  { left: 37px; width: 474px; border-radius: 28px 0 0 28px; }

  .brand { position: absolute; display: flex; align-items: center; gap: 8px;
           color: var(--gold); font-weight: 600; font-size: 19px; white-space: nowrap; }
  .brand__dot { width: 14px; height: 14px; border-radius: 50%; background: var(--gold); flex: none; }
  .card--front .brand { left: 120px; top: 164px; transform: translateX(-50%); }
  .card--back .brand  { left: 140px; top: 164px; transform: translateX(-50%); }

  .tagline { position: absolute; left: 256px; width: 255px; text-align: center; }
  .tagline__title { font-family: "Allura", cursive; color: var(--paper); font-size: 50px; line-height: 1; margin-top: 112px; }
  .tagline__text { font-size: 15px; line-height: 18px; margin-top: 22px; }

  .contact { position: absolute; left: 240px; top: 88px; }
  .contact__name { font-family: "Allura", cursive; color: var(--sand); font-size: 32px; line-height: 1; margin-bottom: 6px; }
  .contact__line { font-size: 17.5px; line-height: 24.5px; white-space: nowrap; }
</style>
</head>
<body>
<main class="canvas">
  <section class="card card--front">
    <div class="panel"></div>
    <div class="brand"><span class="brand__dot"></span>Ruhe im Kreis</div>
    <div class="tagline">
      <p class="tagline__title">Yogakurse</p>
      <p class="tagline__text">für Beginner, Schwangere<br>und frischgebackene Mamas</p>
    </div>
  </section>

  <section class="card card--back">
    <div class="panel"></div>
    <div class="brand"><span class="brand__dot"></span>Ruhe im Kreis</div>
    <div class="contact">
      <p class="contact__name">Ruhe im Kreis</p>
      <p class="contact__line">Yoga &amp; Beckenbodentraining</p>
      <p class="contact__line">Mareike Holsten</p>
      <p class="contact__line">01529447180</p>
      <p class="contact__line">info@ruhe-im-kreis-beispiel.de</p>
      <p class="contact__line">www.ruhe-im-kreis-beispiel.de</p>
    </div>
  </section>
</main>
</body>
</html>
```